Dynamic Website Design For Dynamic Speaker and Business Coach!

Professional Website Design for a for a Professional Business coach, Business trainer, and Speaker.

Note: This is for design only. No coding required. We want to see your ideas for a great website! This will be a FUN design and not boring like others you may work on.

Please let your creative ideas flow. We have given you a ton of info along with videos to help you understand what we are after, however we WANT your creativity to shine through in your designs!

We are a professional company that has run hundreds of crowdsourced projects on multiple platforms. If you participate in this contest (we hope you do) you can expect great video feedback, consistent feedback, and also our guarantee that if we know your website design will not be what we are looking for we will notify you so you don’t waste your time if there is no chance of you winning.

We respect and recognize this is how you make your living and we will not play games. We look forward to an awesome contest and awesome website designs.

Design Brief:

We are looking for a fresh and fun new design for

http://www.brightpath-advisory.net

This individual (Dana Holloway) teaches and trains corporations and businesses in the fields of leadership, sales, communication, business operations etc. Additionally this business teaches and mentors business professionals in a small group level or 1 on 1.

The website needs to convey trust, professionalism, and affluent, while at the same time having some personality!

This business operates on 3 core principles that we would like to see incorporated into the logo if it is a good fit. The 3 principals are:

Focus
Accountability
Results

Here is a video to help explain what we like about the current site and what we don’t like:
http://clipvault.example/t/QwpLmr82kTnb

As you can see the website is geared towards business professionals. Please look over the website to learn what they do. Obviously this is not a good website so we need your help.

We want a website that is professional-looking, has personality and is geared more towards promoting Dana Holloway, the owner of Summit Path Advisory as a Speaker and Business Consultant. The more you can incorporate clean, professional and fun personality elements into the design, the better off you are at winning.

Here are some examples of other sites in their business that have some things we like:

http://velvetcompass.com Please watch video to learn what we like and don’t like:
http://clipvault.example/t/NrtHq7YpLwc

http://tallpinegrowth.com Please watch video to learn what we like and don’t like:
http://clipvault.example/t/J8vDkrWa

http://www.marthaquince.com Please watch video to learn what we like and don’t like:
http://clipvault.example/t/Pz3mx9Rb2Kq

http://www.vantix7.com Please watch video to learn what we like and don’t like:
http://clipvault.example/t/7Gwe4sNhydv

NOTE: We do not want to copy anything outright. We want to learn, model and take their ideas and make them better. We also want to be flexible and take what we like along with your creativity to make an amazing design.

Here is what we are looking for in more specific terms:

Colors: We like the darker blue (not the light blue like the site) and also a burnt orange. I’ve attached her Logo so you can get an idea and feel for the colors.

When looking at colors please know that the current site and look is NOT what we are going for. We are going for a clean and professional look but also a look that is BOLD, FUN, and Vibrant (hence the colors).

Menu: Horizontal. We like bold and easy to read menu items. Don’t make it small and cluttered.

Site Structure: Clean and easy to navigate. We have a lot of content to display so we need a clean structure that breaks up the text and content areas.
Images: Please pull images from the current site. We can always replace the images of course, but if you show them “their own stuff” in the new design you will be closer to winning because it will feel more like “them”

Look and Feel: Professional. Fun. High-End. Business-like. This website needs to convey that Dana Holloway and Summit Path Advisory are professional. That Dana Holloway is a sought-after Speaker and Business Consultant who knows what she is talking about; can be serious when she needs to be, but also likes to have fun with her clients. This site must convey that!

Content Areas: It is a safe bet that if it is on the current site we need it on the new site. So don’t drop anything as it makes it hard to “cut content”.

What we don't want: We do not want clutter, boring, or templates or themes. We don’t want too cartoony, too cute, or too fancy… Be creative!

Out of respect to professional designers who really are working hard to win if you do not follow this brief, you submit worn out themes, templates, or boring designs you will be eliminated. We are offering great prize money for this so we expect great visual designs.
Updates

Project Deadline Extended
Reason: Our client is out of town, and waiting to hear feedback from them. So, in the meantime, we wanted to keep the project going to see what else you designers can come up with. As soon as we hear back from our client, we will pass along the info. Thanks!

Target Market(s)

Target Audience is entrepreneurs and business professionals alike. This is all business to business stuff.

This person teaches and trains startups and billion dollar companies. The common thread is that they are all businesses and companies who need help in various areas including sales, communication, business operations, etc.

Industry/Entity Type

Business

Font styles to use
Sans Serif

Requirements
Must have
• Brief is very detailed. Please review
Nice to have
Should not have

```html
<!DOCTYPE html>
<html lang="en">
<head>
<meta charset="utf-8">
<title>Summit Path Advisory — Albuquerque Business Coaching</title>
<link href="https://fonts.googleapis.com/css2?family=Lato:ital,wght@0,400;0,700;0,900;1,400;1,700&display=swap" rel="stylesheet">
<style>
:root{
  --blue:#1f5fae;
  --navy:#14306b;
  --nav:#1d73c0;
  --orange:#e8852b;
  --burnt:#d9762a;
  --coral:#f07167;
  --sky:#6aaedc;
  --pale:#eaf3fb;
  --cream:#fdf6e4;
  --ink:#1b1b1b;
  --line:#d9b48f;
}
*{box-sizing:border-box;margin:0;padding:0}
html,body{width:1200px;height:3251px;overflow:hidden;background:#fff}
body{font-family:'Lato',sans-serif;color:var(--ink);position:relative}
.abs{position:absolute}

/* header */
.brand{left:40px;top:44px;display:flex;align-items:center;gap:14px}
.brand-dot{width:70px;height:70px;border-radius:50%;background:var(--orange)}
.brand-name{font-size:38px;font-weight:900;color:var(--blue);line-height:1}
.owner-photo{left:393px;top:38px;width:62px;height:100px;background:linear-gradient(#5c7fa3,#2c3e58)}
.social{display:flex;gap:26px}
.social span{width:42px;height:42px;border-radius:50%;background:var(--blue);display:block}
.social span:nth-child(2){background:#2aa3e0}
.social span:nth-child(3){background:#1574b0}
.header-social{left:543px;top:93px}
.phone{right:55px;top:44px;display:flex;align-items:center;gap:10px;font-size:28px;color:var(--orange)}
.search{left:813px;top:93px;width:340px;height:42px;border:1px solid #cfcfcf;border-radius:3px;display:flex;align-items:center;justify-content:space-between;padding:0 12px;font-size:15px;color:#777}

/* nav */
.nav{left:22px;top:171px;width:1159px;height:54px;background:var(--nav);display:flex;align-items:stretch;justify-content:space-between;padding-right:14px;box-shadow:0 3px 5px rgba(0,0,0,.25)}
.nav a{color:#fff;text-decoration:none;font-size:14px;font-weight:700;display:flex;align-items:center;white-space:nowrap;letter-spacing:.2px}
.nav a.current{background:var(--burnt);padding:0 30px}

/* intro */
.page-title{left:49px;top:294px;font-size:22px;color:var(--orange);font-weight:400}
.video{left:49px;top:339px;width:569px;height:392px;border-radius:14px;background:#111;padding:14px 14px 40px}
.video-screen{width:100%;height:100%;background:linear-gradient(120deg,#2a5d9c,#1b3b6b 60%,#3c6fa8);position:relative;padding:46px 30px;color:#fff;font-size:44px;font-weight:700;line-height:1.12}
.video-bar{position:absolute;left:0;right:0;bottom:0;height:32px;background:rgba(0,0,0,.6)}
.video-stand{left:230px;top:731px;width:210px;height:10px;background:#bbb;border-radius:0 0 8px 8px}

.signup-lead{left:820px;top:315px;width:350px;text-align:center;color:var(--orange)}
.signup-lead h3{font-size:13px;font-weight:700}
.signup-lead p{font-size:9px;margin-top:8px;line-height:1.7}
.signup-card{left:856px;top:401px;width:271px;height:290px;background:var(--sky);border:5px solid var(--pale);padding:18px 22px}
.field{height:40px;background:#fff;border-radius:3px;margin-bottom:22px;display:flex;align-items:center;gap:10px;padding:0 12px;font-size:15px;color:#555}
.btn{height:46px;background:var(--coral);color:#fff;font-size:19px;font-weight:700;display:flex;align-items:center;justify-content:center;border-radius:3px}
.signup-card small{display:block;text-align:center;font-size:10px;color:#fff;margin:12px 0}
.connects{display:flex;gap:12px}
.connects span{flex:1;height:32px;border-radius:3px;background:#3b5a9a;color:#fff;font-size:12px;font-weight:700;display:flex;align-items:center;justify-content:center}
.connects span:last-child{background:#3fb1e8}

/* principles */
.rule{left:122px;width:956px;height:2px;background:var(--line)}
.principles-title{left:0;width:1200px;top:834px;text-align:center;color:var(--blue);font-size:26px;font-weight:700;font-variant:small-caps}
.principle{width:140px;text-align:center;top:878px}
.principle b{display:block;font-size:13px;font-weight:400;font-variant:small-caps;color:var(--blue)}
.principle.hot b{color:var(--orange)}
.principle i{display:block;margin:30px auto 0;width:82px;height:82px;border-radius:50%;background:radial-gradient(circle at 40% 40%,#f6f6f6,#a7a7a7);border:3px solid #777}
.principle.hot i{border-color:var(--orange);background:radial-gradient(circle at 40% 40%,#fff,#e59a55)}

/* copy */
.copy{left:127px;top:1116px;width:950px;font-size:21px;line-height:30px;text-transform:uppercase;hyphens:auto}
.copy p{margin-bottom:30px}
.copy strong{font-weight:900}

/* feature boxes */
.feature{top:1872px;height:385px;border:3px solid var(--orange);border-radius:6px;box-shadow:0 8px 14px rgba(0,0,0,.25);padding:20px 30px}
.feature h4{text-align:center;color:var(--blue);font-size:21px;font-weight:900;text-transform:uppercase;line-height:1.2;margin-bottom:16px}
.feature ul{padding-left:22px;font-size:14px;line-height:1.6;text-transform:uppercase}

/* testimonial */
.testimonial{left:60px;top:2352px;width:1078px;height:227px;background:radial-gradient(ellipse at 50% 60%,#fff 0%,var(--cream) 55%,#f4e4b6 100%);box-shadow:0 8px 14px rgba(0,0,0,.25);text-align:center;padding:34px 150px 0}
.testimonial h3{font-size:23px;font-weight:400;color:#222;letter-spacing:.5px}
.testimonial blockquote{font-style:italic;color:var(--blue);font-weight:700;font-size:13px;line-height:1.6;margin-top:20px;text-align:left}
.testimonial cite{display:block;text-align:right;font-size:10px;color:#444;font-style:normal;margin-top:4px}
.more{display:inline-block;margin-top:8px;background:var(--orange);color:#fff;font-size:10px;font-weight:700;padding:4px 14px;border-radius:3px}
.arrow{top:2446px;width:36px;height:36px;background:#a9a9a9}

/* about */
.about-band{left:60px;top:2669px;width:1078px;height:360px;background:var(--sky);box-shadow:0 8px 14px rgba(0,0,0,.25)}
.about{left:154px;top:2722px;width:897px;height:230px;background:#fff;box-shadow:0 3px 8px rgba(0,0,0,.25);display:flex}
.about-left{flex:0 0 540px;position:relative}
.about-left h5{font-size:19px;font-style:italic;color:var(--navy);font-weight:700;position:absolute;left:40px;top:26px}
.about-photo{position:absolute;left:30px;top:74px;width:104px;height:104px;border-radius:50%;background:linear-gradient(#8a6b55,#3e2c25);border:3px solid var(--burnt)}
.about-text{position:absolute;left:152px;top:66px;width:370px}
.about-text b{font-size:11px;font-style:italic;color:var(--navy)}
.about-text p{font-size:10px;font-style:italic;color:#444;line-height:1.5;margin-top:8px}
.about-right{flex:1;border-left:2px solid #ddd;margin:20px 0;padding:0 24px}
.about-right h5{font-size:20px;color:var(--navy);font-weight:400;font-style:italic;margin-top:4px}
.about-right h5 em{color:var(--orange)}
.mini{height:26px;border:1px solid #ddd;margin:16px 20px 0;font-size:10px;color:#777;display:flex;align-items:center;padding:0 10px}
.mini-btn{margin:18px 20px 0;height:36px;background:var(--coral);color:#fff;font-size:14px;font-weight:700;display:flex;align-items:center;justify-content:center;border-radius:3px}

/* footer */
.foot-nav{left:100px;width:660px;font-size:13px;display:flex;justify-content:center}
.foot-nav span{padding:0 14px;border-right:2px solid var(--orange);white-space:nowrap}
.foot-nav span:last-child{border-right:0}
.footer-social{left:923px;top:3081px}
.copyright{left:0;width:1200px;top:3182px;text-align:center;font-size:13px;font-weight:700}
</style>
</head>
<body>

<header>
  <div class="abs brand">
    <span class="brand-dot"></span>
    <div class="brand-name">Summit Path<br>Advisory</div>
  </div>
  <div class="abs owner-photo" role="img" aria-label="Portrait of Dana Holloway"></div>
  <div class="abs social header-social" aria-label="Social links"><span></span><span></span><span></span></div>
  <div class="abs phone">
    <svg width="22" height="34" viewBox="0 0 22 34"><rect x="2" y="2" width="18" height="30" rx="3" fill="#f4b230"/><rect x="5" y="6" width="12" height="10" fill="#fff"/></svg>
    (505) 555-0182
  </div>
  <div class="abs search">Enter your search term... <svg width="18" height="18" viewBox="0 0 18 18"><circle cx="7" cy="7" r="5.5" fill="none" stroke="#666" stroke-width="2"/><line x1="11" y1="11" x2="16" y2="16" stroke="#666" stroke-width="2"/></svg></div>
</header>

<nav class="abs nav">
  <a class="current">HOME</a><a>PASSION</a><a>WHO WE ARE</a><a>SPEAKER</a><a>FREE VIDEOS</a><a>WEB TV SHOW</a><a>TESTIMONIALS</a><a>MERIDIAN LEARNING</a><a>BLOG</a><a>CONTACT</a>
</nav>

<h1 class="abs page-title">ALBUQUERQUE BUSINESS COACHING AND CONSULTING</h1>

<div class="abs video">
  <div class="video-screen" role="img" aria-label="Intro video with Dana Holloway presenting">
    Do You Need<br>More Focus,<br>Accountability<br>&amp; Results?
    <div class="video-bar"></div>
  </div>
</div>
<div class="abs video-stand"></div>

<div class="abs signup-lead">
  <h3>CHANGE YOUR THINKING, CHANGE YOUR RESULTS!</h3>
  <p>SIGN UP FOR MY FREE REPORT "WHEN YOUR GOALS STALL"<br>AND HAVE MORE RESULTS THIS MONTH</p>
</div>
<div class="abs signup-card">
  <div class="field">👤 Name</div>
  <div class="field">✉ Email</div>
  <div class="btn">Sign me up!</div>
  <small>...or sign up with your social media account</small>
  <div class="connects"><span>Connect</span><span>Connect</span></div>
</div>

<div class="abs rule" style="top:813px"></div>
<h2 class="abs principles-title">Our 3 Core Principles</h2>
<div class="abs principle" style="left:345px"><b>Focus</b><i role="img" aria-label="Focus icon"></i></div>
<div class="abs principle hot" style="left:559px"><b>Accountability</b><i role="img" aria-label="Accountability icon"></i></div>
<div class="abs principle" style="left:778px"><b>Results</b><i role="img" aria-label="Results icon"></i></div>
<div class="abs rule" style="top:1046px"></div>

<section class="abs copy" lang="en">
  <p>Are you searching to bridge the gap between where you are and where you want to be?</p>
  <p>As you face greater pressure to "move the needle" on your company's productivity and bottom line profitability, how prepared are you to step in and shine as the leader?</p>
  <p>We specialize in guiding leaders to become easier to follow. You're in the right place.</p>
  <p>Whether you're leading a company, or are an employee, all of us have a role to play in contributing to the profit and the future of the company.</p>
  <p><strong>Your organization expects you to deliver value by delivering results.</strong></p>
  <p>At Summit Path Advisory, we know as a company or as individuals, clarity of the direction captured in an annual plan that is monitored monthly is one of the surest, quickest and most profitable ways of getting ahead in these challenging times.</p>
  <p>What is the missing link in your business? What are you searching for? Email me today, conversation is complimentary to investigate where we start building the business you envision for tomorrow.</p>
</section>

<div class="abs feature" style="left:68px;width:515px">
  <h4>Albuquerque Business Coach:<br>Focus, Accountability, &amp; Results</h4>
  <ul>
    <li>Development of an operational plan that links all departments</li>
    <li>Implementation and monitoring individual and departmental plans</li>
    <li>Diagnosing employee training needs</li>
    <li>Delivering the training to develop leaders and staff</li>
    <li>Coach leaders, individuals and teams whether you're leading a company, or are an employee, all of us have a role to play in contributing to the profit and the future of the company.</li>
  </ul>
</div>
<div class="abs feature" style="left:618px;width:520px">
  <h4>Summit Path Advisory has delivered on our promise. Our clients learn to:</h4>
  <ul>
    <li>Establish new patterns of productivity for the business</li>
    <li>Clarification of future goals, targets and benchmarks</li>
    <li>Implement actionable steps around short, medium and long term goals</li>
    <li>Identify roadblocks and disempowering habits</li>
    <li>Create a repeatable process that delivers results</li>
    <li>Transform burned out employees or leaders into fired-up employees</li>
  </ul>
</div>

<section class="abs testimonial">
  <h3>WHAT OUR CLIENTS SAY ABOUT US</h3>
  <blockquote>"I don't know a single person in Albuquerque who can network like Dana Holloway. She is truly in a league of her own with respect to making human connections. Every time I attend one of her seminars, I get valuable information for running my business and I notice that Dana is always on her way..."</blockquote>
  <cite>~Mark Ellison - President of Cedar Lane Home Care</cite>
  <span class="more">Read More</span>
</section>
<svg class="abs arrow" style="left:146px" viewBox="0 0 36 36"><path d="M20 10l-8 8 8 8M28 10l-8 8 8 8" fill="none" stroke="#fff" stroke-width="3"/></svg>
<svg class="abs arrow" style="left:1018px" viewBox="0 0 36 36"><path d="M8 10l8 8-8 8M16 10l8 8-8 8" fill="none" stroke="#fff" stroke-width="3"/></svg>

<div class="abs about-band"></div>
<section class="abs about">
  <div class="about-left">
    <h5>Hi, I'm Dana</h5>
    <div class="about-photo" role="img" aria-label="Portrait of Dana Holloway"></div>
    <div class="about-text">
      <b>Professional Business Coach &nbsp;|&nbsp; Business Trainer &nbsp;|&nbsp; Speaker</b>
      <p>Lorem ipsum dolor sit amet, consectetur adipiscing elit. Aliquam aliquam lectus nec velit ullamcorper blandit laoreet et sapien. Quisque posuere finibus pellentesque. Nullam ipsum felis, scelerisque eget tempor et, varius sit amet sapien. Nam tincidunt justo efficitur.</p>
      <span class="more">Read More</span>
    </div>
  </div>
  <div class="about-right">
    <h5>Be sure to <em>Sign Up</em> for my <em>Blog!</em></h5>
    <div class="mini">Name</div>
    <div class="mini">Email</div>
    <div class="mini-btn">Sign me up!</div>
  </div>
</section>

<footer>
  <div class="abs foot-nav" style="top:3080px"><span>HOME</span><span>PASSION</span><span>WHO WE ARE</span><span>SPEAKER</span><span>FREE VIDEOS</span></div>
  <div class="abs foot-nav" style="top:3106px"><span>WEB TV SHOW</span><span>TESTIMONIALS</span><span>MERIDIAN LEARNING</span><span>BLOG</span><span>CONTACT</span></div>
  <div class="abs social footer-social"><span></span><span></span><span></span></div>
  <div class="abs copyright">Copyright © 2014 &nbsp;Summit Path Advisory &nbsp;|&nbsp; All rights reserved</div>
</footer>

</body>
</html>
```